Calvanta Group Real Estate Company business cards

New business card design, we are generally happy with the basic layout of the existing front of business card, (feel free to change) but require a head shot photo on the back side.

http://www.calvanta.com.au/

Attached logos, and existing business card

------------------------------

Target Market(s)

Real estate

Industry/Entity Type

Real Estate

Contact Information for Business Card

Standard size double sided

Font styles to use
Other font styles liked:
• Futura

Requirements
Must have
• Photo head shot on the back side
Nice to have
• yes
Should not have
• No

```html
<!DOCTYPE html>
<html lang="en">
<head>
<meta charset="utf-8">
<title>Calvanta Group – Business Cards</title>
<link href="https://fonts.googleapis.com/css2?family=Jost:wght@400;500;600;700&display=swap" rel="stylesheet">
<style>
  :root{
    --backdrop:#2a2a2c;
    --card-grey:#8b8c8e;
    --card-white:#ffffff;
    --purple:#2e1d63;
    --orange:#f0901e;
    --muted:#9a9a9a;
    --ink:#2e1d63;
    --photo-light:#e6e8ea;
    --photo-dark:#3a4a6a;
  }
  *{box-sizing:border-box;margin:0;padding:0}
  html,body{width:1200px;height:900px;overflow:hidden;background:var(--backdrop);font-family:"Jost",Futura,sans-serif}
  .canvas{position:relative;width:1200px;height:900px}
  .card{position:absolute;width:540px;height:309px;top:296px;box-shadow:0 10px 30px rgba(0,0,0,.45)}

  /* Grey card */
  .card--brand{left:40px;background:var(--card-grey);display:flex;flex-direction:column;align-items:center;justify-content:center}
  .brand-name{font-size:88px;font-weight:500;color:var(--purple);letter-spacing:-1px;line-height:1}
  .brand-services{margin-top:14px;font-size:19px;font-weight:600;letter-spacing:3px;color:var(--orange)}
  .brand-services .sep{color:#fff;padding:0 4px}
  .brand-web{margin-top:6px;font-size:20px;font-weight:600;letter-spacing:1px;color:var(--orange)}
  .brand-web b{color:#fff;font-weight:700}

  /* White card */
  .card--contact{left:620px;background:var(--card-white);overflow:hidden}
  .side-band{position:absolute;left:26px;top:0;width:30px;height:100%;background:var(--purple)}
  .logo-block{position:absolute;left:80px;top:30px}
  .logo-name{font-size:66px;font-weight:500;color:var(--purple);line-height:1;letter-spacing:-1px}
  .logo-group{position:absolute;right:4px;top:64px;font-size:9px;letter-spacing:5px;color:var(--muted)}
  .tagline{margin-top:14px;font-size:22px;color:var(--purple)}
  .person{position:absolute;left:120px;top:172px}
  .person-name{font-size:26px;font-weight:700;color:var(--purple);letter-spacing:.5px;line-height:1}
  .person-role{font-size:15px;color:var(--orange);font-weight:500;margin-top:2px}
  .contact-list{list-style:none;margin-top:2px;font-size:14px;color:var(--ink)}
  .contact-list li{display:flex;align-items:center;gap:7px;line-height:1.3}
  .contact-list .label{color:var(--orange)}
  .contact-list svg{width:12px;height:12px;flex:none}
  .headshot{position:absolute;right:28px;top:28px;width:150px;height:150px;border-radius:50%;border:2px solid var(--purple);
    background:radial-gradient(circle at 50% 40%,var(--photo-light) 0 45%,var(--photo-dark) 100%)}
</style>
</head>
<body>
<main class="canvas">
  <section class="card card--brand">
    <div class="brand-name">calvanta</div>
    <div class="brand-services">Buy <span class="sep">|</span> Sell <span class="sep">|</span> Rent</div>
    <div class="brand-web">www.<b>calvanta.com</b>.au</div>
  </section>

  <section class="card card--contact">
    <div class="side-band"></div>
    <div class="logo-block">
      <div class="logo-name">calvanta</div>
      <div class="logo-group">GROUP</div>
      <div class="tagline">your next move starts here</div>
    </div>
    <div class="headshot" role="img" aria-label="Head shot photo of the director in a suit"></div>
    <div class="person">
      <div class="person-name">DANIEL TRAN</div>
      <div class="person-role">DIRECTOR</div>
      <ul class="contact-list">
        <li><span class="label">ABN:</span> 12 345 678 901</li>
        <li>
          <svg viewBox="0 0 12 12"><rect x="3" y="1" width="6" height="10" rx="1" fill="none" stroke="#f0901e" stroke-width="1.4"/><circle cx="6" cy="9" r=".7" fill="#f0901e"/></svg>
          0400 555 318
        </li>
        <li>
          <svg viewBox="0 0 12 12"><rect x="1" y="2.5" width="10" height="7" fill="none" stroke="#f0901e" stroke-width="1.3"/><path d="M1 2.5l5 4 5-4" fill="none" stroke="#f0901e" stroke-width="1.3"/></svg>
          daniel.tran@calvanta.com.au
        </li>
        <li>
          <svg viewBox="0 0 12 12"><circle cx="6" cy="6" r="5" fill="none" stroke="#f0901e" stroke-width="1.2"/><ellipse cx="6" cy="6" rx="2.2" ry="5" fill="none" stroke="#f0901e" stroke-width="1"/><path d="M1 6h10" stroke="#f0901e" stroke-width="1"/></svg>
          www.calvanta.com.au
        </li>
      </ul>
    </div>
  </section>
</main>
</body>
</html>
```